Letterhead

Create letterhead for corporate letters, proposals, thank yous, etc.

Target Market(s)

Technology, Communications

Industry/Entity Type

Information Technology

```html
<!DOCTYPE html>
<html lang="en">
<head>
<meta charset="utf-8">
<title>Tiervale Letterhead</title>
<link rel="stylesheet" href="https://fonts.googleapis.com/css2?family=Montserrat:wght@300&family=Open+Sans:wght@400;600&display=swap">
<style>
  :root {
    --backdrop: #e4e4e4;
    --paper: #ffffff;
    --ink: #2b2b2b;
    --brand-grey: #8a8f94;
    --brand-blue: #1f8fd0;
    --rule: #d9d9d9;
    --watermark: #f1f1f1;
  }
  * { margin: 0; padding: 0; box-sizing: border-box; }
  html, body {
    width: 831px; height: 1200px; overflow: hidden;
    background: var(--backdrop);
  }
  .sheet {
    position: absolute; left: 44px; top: 28px;
    width: 743px; height: 1135px;
    background: var(--paper);
    overflow: hidden;
    font-family: "Open Sans", Arial, sans-serif;
    color: var(--ink);
  }
  .brand {
    position: absolute; left: 28px; top: 42px;
    display: flex; align-items: center; gap: 12px;
  }
  .brand-dot {
    width: 30px; height: 30px; border-radius: 50%;
    background: var(--brand-blue);
  }
  .brand-name {
    font-family: "Montserrat", Arial, sans-serif;
    font-weight: 300; font-size: 42px; letter-spacing: 1px;
    color: var(--brand-grey);
  }
  .contact {
    position: absolute; right: 34px; top: 30px;
    list-style: none; text-align: right;
    font-size: 12.5px; line-height: 19.5px;
  }
  .contact li { display: flex; justify-content: flex-end; align-items: center; gap: 8px; }
  .contact svg { width: 11px; height: 11px; fill: var(--brand-blue); }
  .header-rule, .footer-rule {
    position: absolute; left: 0; right: 0; height: 1px; background: var(--rule);
  }
  .header-rule { top: 116px; }
  .footer-rule { top: 1066px; }
  .watermark {
    position: absolute; left: 30px; top: 560px;
    font-family: "Montserrat", Arial, sans-serif;
    font-weight: 300; font-size: 150px; color: var(--watermark);
    transform: rotate(-33deg); transform-origin: left center;
    white-space: nowrap; user-select: none;
  }
  .footer {
    position: absolute; left: 0; right: 0; top: 1076px;
    text-align: center; font-size: 11.5px; line-height: 17px;
  }
  .footer-label { color: var(--brand-blue); font-weight: 600; }
</style>
</head>
<body>
  <div class="sheet">
    <div class="brand">
      <span class="brand-dot"></span>
      <span class="brand-name">Tiervale</span>
    </div>

    <ul class="contact">
      <li>123-456-7890
        <svg viewBox="0 0 24 24"><path d="M6.6 10.8a15 15 0 0 0 6.6 6.6l2.2-2.2a1 1 0 0 1 1-.25 11.4 11.4 0 0 0 3.6.57 1 1 0 0 1 1 1V20a1 1 0 0 1-1 1A17 17 0 0 1 3 4a1 1 0 0 1 1-1h3.5a1 1 0 0 1 1 1c0 1.25.2 2.45.57 3.57a1 1 0 0 1-.25 1z"/></svg>
      </li>
      <li>123-456-7890
        <svg viewBox="0 0 24 24"><rect x="6" y="1" width="12" height="22" rx="2.5"/><rect x="8" y="4" width="8" height="13" fill="#fff"/></svg>
      </li>
      <li>info@companyname.com
        <svg viewBox="0 0 24 24"><rect x="1" y="4" width="22" height="16" rx="2"/><path d="M2 6l10 7 10-7" fill="none" stroke="#fff" stroke-width="2"/></svg>
      </li>
      <li>www.companyname.com
        <svg viewBox="0 0 24 24"><circle cx="12" cy="12" r="11"/><path d="M1 12h22M12 1c4 4 4 18 0 22M12 1c-4 4-4 18 0 22" fill="none" stroke="#fff" stroke-width="1.6"/></svg>
      </li>
    </ul>

    <div class="header-rule"></div>

    <div class="watermark" aria-hidden="true">Tiervale</div>

    <div class="footer-rule"></div>
    <footer class="footer">
      <div class="footer-label">Address</div>
      <div>Address Line1, Address Line2, Country 123456</div>
    </footer>
  </div>
</body>
</html>
```